TK & LJ Shearing Pty Ltd

We already have an existing logo created by Lumen Guild however we have restructured to a company. We would like someone to add Pty Ltd to our business name please.

Colors

Designer to choose only greyscale colors for use in the design.

```html
<!DOCTYPE html>
<html lang="en">
<head>
<meta charset="utf-8">
<title>TK &amp; LJ Shearing Pty Ltd — Business Card</title>
<link rel="stylesheet" href="https://fonts.googleapis.com/css2?family=Lato:wght@400;700&display=swap">
<style>
  :root {
    --backdrop: #2b2b2b;
    --card: #050709;
    --ink: #ffffff;
    --rule: #d9d9d9;
  }
  * { margin: 0; padding: 0; box-sizing: border-box; }
  html, body {
    width: 1200px;
    height: 750px;
    overflow: hidden;
    background: var(--backdrop);
  }
  .stage {
    position: relative;
    width: 1200px;
    height: 750px;
  }
  .business-card {
    position: absolute;
    left: 307px;
    top: 207px;
    width: 587px;
    height: 335px;
    background: var(--card);
    color: var(--ink);
    font-family: "Lato", sans-serif;
  }
  .brand {
    position: absolute;
    left: 122px;
    top: 30px;
    width: 344px;
    text-align: center;
    font-weight: 700;
    color: var(--ink);
    line-height: 1;
  }
  .brand-initials {
    display: block;
    font-size: 78px;
    letter-spacing: 1px;
  }
  .brand-descriptor {
    display: block;
    margin-top: 16px;
    font-size: 30px;
    letter-spacing: 0.5px;
  }
  .contact-divider {
    position: absolute;
    left: 122px;
    top: 189px;
    width: 343px;
    height: 24px;
  }
  .contact-details {
    position: absolute;
    left: 0;
    top: 226px;
    width: 100%;
    text-align: center;
    font-size: 17.5px;
    line-height: 24.8px;
    font-weight: 400;
  }
</style>
</head>
<body>
<main class="stage">
  <section class="business-card" aria-label="TK &amp; LJ Shearing Pty Ltd business card">
    <h1 class="brand">
      <span class="brand-initials">TK &amp; LJ</span>
      <span class="brand-descriptor">SHEARING PTY LTD</span>
    </h1>

    <svg class="contact-divider" viewBox="0 0 343 24" aria-hidden="true">
      <line x1="0" y1="11.5" x2="133" y2="11.5" stroke="var(--rule)" stroke-width="1"/>
      <line x1="210" y1="11.5" x2="343" y2="11.5" stroke="var(--rule)" stroke-width="1"/>
      <!-- location -->
      <circle cx="145" cy="12" r="11.5" fill="var(--ink)"/>
      <path d="M145 4.5a5 5 0 0 0-5 5c0 3.8 5 9.5 5 9.5s5-5.7 5-9.5a5 5 0 0 0-5-5z" fill="var(--card)"/>
      <circle cx="145" cy="9.6" r="1.9" fill="var(--ink)"/>
      <!-- phone -->
      <circle cx="171.5" cy="12" r="11.5" fill="var(--ink)"/>
      <path d="M166.4 5.2l2.2-.6 1.5 3.6-1.5 1.2a9 9 0 0 0 4 4l1.2-1.5 3.6 1.5-.6 2.2c-.3 1-1.3 1.6-2.4 1.3-4.3-1.1-7.7-4.5-8.8-8.8-.3-1.1.3-2.1 1.3-2.4z" fill="var(--card)"/>
      <!-- email -->
      <circle cx="198" cy="12" r="11.5" fill="var(--ink)"/>
      <rect x="191.5" y="7.5" width="13" height="9" rx="1" fill="var(--card)"/>
      <path d="M192 8.2l6 4.6 6-4.6M192 16l4.3-3.6M204 16l-4.3-3.6" stroke="var(--ink)" stroke-width="0.9" fill="none"/>
    </svg>

    <address class="contact-details" style="font-style: normal;">
      PO Box 318 KELLBROOK WA 6590<br>
      Tom 0400 000 000<br>
      tkljshearing@example.com
    </address>
  </section>
</main>
</body>
</html>
```